Life Coach for Lawyers Business Card Design

Elegant, original, business card design for life coaching service for associate attorneys who work in big law and struggle with stress, overwhelm, and time management. Double sided design.

Target Market(s)

Women associate attorneys who work in big law and struggle with stress, overwhelm, and time management.

Industry/Entity Type

Life Coaching

Contact Information for Business Card

Marissa Pendrell
Life Coach
518.677.3941
calmbriefcounsel.net
marissa@calmbriefcounsel.net
@calmbriefcounsel (Instagram)

Font styles to use
Other font styles liked:
• Silver South font duo. See uploaded files.

Requirements
Must have
• Icons for phone, website, email, and Instagram instead of words. Specific colors used in my logo (171B2B, 421121, FFFFFF)
Nice to have
• Foil. Embossed. Feminine design.
Should not have
• Any colors other than those used in logo. See uploaded files.

```html
<!DOCTYPE html>
<html lang="en">
<head>
<meta charset="UTF-8">
<title>Calm Brief Counsel – Business Card</title>
<link rel="stylesheet" href="https://fonts.googleapis.com/css2?family=Roboto:wght@400;500;700&display=swap">
<style>
  :root {
    --stage: #2b2c30;
    --card: #171b2b;
    --wine: #421121;
    --white: #ffffff;
    --soft: rgba(255,255,255,0.82);
  }
  * { margin: 0; padding: 0; box-sizing: border-box; }
  html, body { width: 1200px; height: 900px; overflow: hidden; }
  body {
    background: var(--stage);
    font-family: "Roboto", Arial, sans-serif;
    color: var(--white);
    display: flex;
    flex-direction: column;
    align-items: center;
    justify-content: center;
    gap: 56px;
  }
  .card {
    position: relative;
    width: 640px;
    height: 366px;
    background: var(--card);
    border-radius: 22px;
    box-shadow: 0 14px 30px rgba(0,0,0,0.35);
  }
  .wordmark {
    position: absolute;
    font-weight: 400;
    text-transform: uppercase;
    letter-spacing: 0.12em;
    line-height: 1;
    white-space: nowrap;
    color: var(--white);
  }
  .rule {
    position: absolute;
    height: 1.5px;
    background: var(--white);
  }
  /* Front */
  .card--front .wordmark { left: 70px; top: 188px; font-size: 24px; }
  .card--front .rule { left: 388px; right: 78px; top: 206px; }

  /* Back */
  .card--back .wordmark { left: 48px; top: 92px; font-size: 17px; }
  .card--back .rule { left: 280px; right: 40px; top: 104px; }
  .identity {
    position: absolute;
    right: 384px;
    top: 150px;
    text-align: right;
  }
  .identity__name { font-size: 19px; font-weight: 700; letter-spacing: 0.01em; }
  .identity__role { font-size: 13px; font-weight: 400; color: var(--soft); margin-top: 4px; }
  .divider {
    position: absolute;
    left: 270px;
    top: 124px;
    width: 1.5px;
    height: 116px;
    background: var(--white);
  }
  .contacts {
    position: absolute;
    left: 288px;
    top: 128px;
    list-style: none;
  }
  .contacts li {
    display: flex;
    align-items: center;
    gap: 10px;
    font-size: 13px;
    height: 26px;
    color: var(--white);
  }
  .contacts svg { width: 13px; height: 13px; flex: none; }
</style>
</head>
<body>
  <section class="card card--front" aria-label="Card front">
    <div class="wordmark">Calm Brief Counsel</div>
    <div class="rule"></div>
  </section>

  <section class="card card--back" aria-label="Card back">
    <div class="wordmark">Calm Brief Counsel</div>
    <div class="rule"></div>

    <div class="identity">
      <p class="identity__name">Marissa Pendrell</p>
      <p class="identity__role">Life Coach</p>
    </div>
    <div class="divider"></div>

    <ul class="contacts">
      <li>
        <svg viewBox="0 0 16 16" aria-hidden="true"><path fill="#fff" d="M3.6 1.5l2.3 2.6-1.3 1.8c.9 2 2.6 3.7 4.6 4.6l1.8-1.3 2.6 2.3-1.3 2.3C6.8 13.6 2.4 9.2 1.3 3z"/></svg>
        518.677.3941
      </li>
      <li>
        <svg viewBox="0 0 16 16" aria-hidden="true"><circle cx="8" cy="8" r="6.6" fill="none" stroke="#fff" stroke-width="1.4"/><ellipse cx="8" cy="8" rx="2.8" ry="6.6" fill="none" stroke="#fff" stroke-width="1.2"/><path d="M1.5 8h13" stroke="#fff" stroke-width="1.2"/></svg>
        calmbriefcounsel.net
      </li>
      <li>
        <svg viewBox="0 0 16 16" aria-hidden="true"><rect x="1" y="3" width="14" height="10" fill="#fff"/><path d="M1 3l7 6 7-6" fill="none" stroke="#171b2b" stroke-width="1.4"/></svg>
        marissa@calmbriefcounsel.net
      </li>
      <li>
        <svg viewBox="0 0 16 16" aria-hidden="true"><circle cx="8" cy="8" r="6" fill="none" stroke="#fff" stroke-width="1.6"/></svg>
        @calmbriefcounsel
      </li>
    </ul>
  </section>
</body>
</html>
```